Update Tender Letter

We have a tender letter for one company however we need to update it to reflect another company of ours "Tanvale Air Conditioning".

The letter needs everything relating to "Morrow Tech" changed to "Tanvale" including, logos, addresses, phone numbers, websites and any background images with Morrow tech to be updated to be a tan vale photo.

I will upload actual photos shortly.

```html
<!DOCTYPE html>
<html lang="en">
<head>
<meta charset="utf-8">
<title>Tanvale Air Conditioning – Tender Submission</title>
<link href="https://fonts.googleapis.com/css2?family=Lato:wght@400;700&family=Montserrat:wght@300;400;600&display=swap" rel="stylesheet">
<style>
:root{
  --stage:#c8cacf;
  --paper:#ffffff;
  --brand-blue:#1d62ad;
  --brand-green:#8dc63f;
  --cyan:#2ab7e6;
  --cover-blue:#3d5f9e;
  --ink:#1f1f1f;
  --rule:#9aa0a8;
  --table-line:#5b7fbf;
}
*{margin:0;padding:0;box-sizing:border-box}
html,body{width:1200px;height:1200px;overflow:hidden}
body{background:var(--stage);position:relative;font-family:"Lato",Arial,sans-serif;color:var(--ink)}
.page{position:absolute;width:259px;height:366px;background:var(--paper);overflow:hidden}
.pg1{left:70px;top:40px}.pg2{left:342px;top:40px}.pg3{left:613px;top:40px}.pg4{left:886px;top:40px}
.pg5{left:70px;top:425px}.pg6{left:342px;top:425px}.pg7{left:613px;top:425px}.pg8{left:886px;top:425px}
.pg9{left:70px;top:808px}.pg10{left:342px;top:808px}.pg11{left:613px;top:808px}

.brand{position:absolute;left:13px;top:13px;display:flex;align-items:center;gap:4px}
.brand-dot{width:9px;height:9px;border-radius:50%;background:var(--brand-green)}
.brand-name{font-family:"Lato",sans-serif;font-weight:700;font-size:13px;color:var(--brand-blue);letter-spacing:.2px}

.band{position:absolute;left:0;top:41px;width:259px;height:77px}
.band-ducts{background:linear-gradient(160deg,#1d2227 0%,#4a525b 45%,#2b3037 70%,#62686f 100%)}
.band-units{background:linear-gradient(180deg,#5c6a78 0%,#d7dbe0 45%,#8e97a1 100%)}
.band-sunset{background:linear-gradient(180deg,#3b4c63 0%,#7d8fa6 40%,#d8c9a9 58%,#3f5a78 72%,#23364d 100%)}
.band-title{position:absolute;left:30px;top:51px;font-family:"Montserrat",sans-serif;font-weight:300;font-size:12.5px;color:var(--cyan);letter-spacing:.4px}
.band-units + .band-title{color:#1a9fd0}

/* cover */
.cover{background:var(--cover-blue)}
.cover-photo{position:absolute;left:0;top:170px;width:259px;height:196px;background:linear-gradient(180deg,rgba(61,95,158,1) 0%,#6f86ad 30%,#9fb0c6 55%,#7a8d8a 75%,#4b5a4f 100%)}
.cover-brand{position:absolute;left:0;right:0;top:46px;display:flex;justify-content:center;align-items:center;gap:6px}
.cover-brand .brand-dot{width:14px;height:14px;background:#fff}
.cover-brand .brand-name{color:#fff;font-size:22px}
.cover-text{position:absolute;left:0;right:0;text-align:center;font-family:"Montserrat",sans-serif}
.cv-tender{top:126px;font-size:15px;color:var(--brand-green);font-weight:400}
.cv-sub{top:150px;font-size:23px;color:var(--brand-green);font-weight:600}
.cv-date{top:183px;font-size:12px;color:#fff;font-weight:400}
.cv-date sup{font-size:7px}
.cv-client{top:203px;font-size:12px;color:var(--cyan);font-weight:600;line-height:16px}

/* about */
.about-photo{position:absolute;left:0;top:41px;width:259px;height:325px;background:linear-gradient(100deg,#2c3442 0%,#3e4a5c 45%,#6d7a8c 70%,#a9b3bf 100%)}
.about-title{position:absolute;left:25px;top:82px;font-family:"Montserrat",sans-serif;font-weight:300;font-size:12.5px;color:var(--cyan)}
.about-body{position:absolute;left:25px;top:102px;width:115px;font-size:3.4px;line-height:5.2px;color:#e6e9ee}
.about-body p{margin-bottom:4px}
.about-body .hl{color:var(--cyan)}

/* body text */
.copy{position:absolute;font-size:3.6px;line-height:5.6px}
.pricing-intro{left:19px;top:124px;width:220px}
.pricing-intro p{margin-bottom:4px}
.price-table{position:absolute;left:19px;top:166px;width:209px;border-collapse:collapse;font-size:3.4px}
.price-table td,.price-table th{border:0.5px solid var(--table-line);height:9.4px;padding:0 2px}
.price-table th{font-weight:700;text-align:center;font-size:3.7px}
.price-table td.amt{text-align:center;width:52px}
.price-table .total td{font-weight:700}
.price-table .total td:first-child{text-align:right}
.words{left:19px;top:316px;width:220px;font-weight:700}

.list-head{font-weight:700;margin-bottom:2px}
.scope-list{padding-left:13px;list-style:decimal}
.scope-list li{padding-left:2px}
.inclusions{left:8px;top:125px;width:240px;line-height:6.5px}
.inclusions .scope-list{font-size:3.4px}
.exclusions{left:8px;top:125px;width:240px;line-height:6.2px}

.form-row{position:absolute;left:32px;width:203px;display:flex;align-items:flex-end;font-size:3.8px;font-weight:700}
.form-row .label{width:58px}
.form-row .line{flex:1;border-bottom:0.5px solid var(--rule);height:3px}
.form-note{position:absolute;left:32px;top:206px;font-size:2.4px}

.qual{left:31px;top:124px;width:206px}
.qual p{margin-bottom:5px}

/* business terms */
.terms-col{position:absolute;font-size:3.3px;line-height:4.7px;color:#222}
.terms-col h4{font-size:3.3px;font-weight:700;margin-top:3px}
.terms-col h4:first-child{margin-top:0}
.bt-a{left:22px;top:124px;width:106px}
.bt-b{left:136px;top:124px;width:108px}

/* full terms pages */
.tc{position:absolute;top:12px;width:108px;font-size:3.55px;line-height:5.15px;color:#222}
.tc h4{font-size:3.55px;font-weight:700;margin-top:4px}
.tc h4:first-child{margin-top:0}
.tc-a{left:24px}.tc-b{left:138px}

/* back */
.back-photo{position:absolute;left:0;top:0;width:259px;height:258px;background:linear-gradient(180deg,#c5ccd4 0%,#8a97a6 35%,#4b79b2 60%,#d7dadd 85%,#b9bec4 100%)}
.back-brand{position:absolute;left:0;right:0;top:280px;display:flex;justify-content:center;align-items:center;gap:5px}
.back-brand .brand-name{font-size:19px}
.back-brand .brand-dot{width:12px;height:12px}
.contact{position:absolute;font-size:3.5px;line-height:13px}
.contact-a{left:13px;top:320px}
.contact-b{left:112px;top:320px}
.badge{position:absolute;left:183px;top:332px;width:58px;height:24px;border-radius:3px;background:#dfe3e8}
</style>
</head>
<body>

<section class="page pg1 cover">
  <div class="cover-photo" role="img" aria-label="Company van parked on a hilltop overlooking a bay with islands"></div>
  <div class="cover-brand"><span class="brand-dot"></span><span class="brand-name">Tanvale</span></div>
  <div class="cover-text cv-tender">TENDER</div>
  <div class="cover-text cv-sub">SUBMISSION</div>
  <div class="cover-text cv-date">26<sup>TH</sup> MAY 2025</div>
  <div class="cover-text cv-client">ST BRIGID'S<br>PROSERPINE</div>
</section>

<section class="page pg2">
  <div class="brand"><span class="brand-dot"></span><span class="brand-name">Tanvale</span></div>
  <div class="about-photo" role="img" aria-label="Technician on a ladder installing a wall-mounted air conditioning unit"></div>
  <h2 class="about-title">ABOUT US /</h2>
  <div class="about-body">
    <p><span class="hl">Tanvale Air</span> provides the full range of air conditioning and mechanical services solutions. From system design right through to installation, commissioning and maintenance our team have wide experience across the commercial, industrial, government, and infrastructure sectors throughout Queensland.</p>
    <p>We have successfully delivered projects for retail precincts, offices, education facilities, airports and hotels, health and aged care, hotels &amp; clubs, and more.</p>
    <p>We're proud of the long-term relationships we've built over the years with our commercial clients. Our attention to detail, comprehensive service offering, and outstanding customer service have helped us build a reputation for reliability and adaptability.</p>
    <p>Since our inception in 2015 we have assembled an expert team whose knowledge and skills are matched by their can-do outlook and approachability. They bring decades of experience to their roles yet they're flexible enough to adapt to and overcome the challenges which are inevitable on any large project.</p>
    <p>You can rest assured our team is always working safely and to the highest standard using only quality brands and materials that meet Australian Standards.</p>
  </div>
</section>

<section class="page pg3">
  <div class="brand"><span class="brand-dot"></span><span class="brand-name">Tanvale</span></div>
  <div class="band band-ducts" role="img" aria-label="Ceiling space with insulated ductwork"></div>
  <h2 class="band-title">PRICING /</h2>
  <div class="copy pricing-intro">
    <p>We offer for your consideration our proposal for the supply, delivery, installation and commissioning of new Air Conditioning and Mechanical services.</p>
    <p>Drawings –<br>Specification –</p>
  </div>
  <table class="price-table">
    <tr><th>BREAKDOWN</th><th>PRICE (EX GST)</th></tr>
    <tr><td>Air Conditioning Equipment</td><td class="amt">$32,454.00</td></tr>
    <tr><td>Ductwork Grilles &amp; Installation</td><td class="amt">$18,909.00</td></tr>
    <tr><td>Pipework &amp; Installation</td><td class="amt">$22,378.00</td></tr>
    <tr><td>Mechanical Electrical</td><td class="amt">$37,012.00</td></tr>
    <tr><td>Fans</td><td class="amt">$3,012.00</td></tr>
    <tr><td>Coatguard Treatment</td><td class="amt">$6,500.00</td></tr>
    <tr><td>Testing &amp; Commissioning</td><td class="amt">$2,600.00</td></tr>
    <tr><td>Warranty &amp; Maintenance</td><td class="amt">$1,850.00</td></tr>
    <tr><td>Documentation, Drawings &amp; Project Management</td><td class="amt">$6,298.00</td></tr>
    <tr><td></td><td class="amt"></td></tr>
    <tr><td></td><td class="amt"></td></tr>
    <tr><td></td><td class="amt"></td></tr>
    <tr class="total"><td>Total Ex GST</td><td class="amt">$131,013.00</td></tr>
  </table>
  <div class="copy words"><span style="font-weight:400">Total in words:</span><br>ONE HUNDRED AND THIRTY-ONE THOUSAND AND THIRTEEN DOLLARS + GST</div>
</section>

<section class="page pg4">
  <div class="brand"><span class="brand-dot"></span><span class="brand-name">Tanvale</span></div>
  <div class="band band-ducts" role="img" aria-label="Roof framing with ductwork under installation"></div>
  <h2 class="band-title">SCOPE OF WORKS /</h2>
  <div class="copy inclusions">
    <div class="list-head">Inclusions:</div>
    <ol class="scope-list">
      <li>Supply, delivery, and installation of new Kairo Electric Air Conditioning systems.</li>
      <li>Allowance has been made for the condensing units to be installed on concrete plinths provided by builder.</li>
      <li>Allowance has been made for all new refrigerant pipework between the indoor fan coil and the external condensing units.</li>
      <li>Allowance has been made for new condensate pipe work from each fan coil unit to a tundish provided by others.</li>
      <li>Allowance has been made for associated Air Conditioning ducting and grills.</li>
      <li>Allowance has been made for one (1) wired proprietary controller per system.</li>
      <li>Allowance has been made for one (1) central controller.</li>
      <li>Supply, delivery and installation of one (1) MSSB.</li>
      <li>Allowance has been made for wiring from MSSB to mechanical equipment.</li>
      <li>Allowance has been made for associated mechanical controls and interlocks.</li>
      <li>Supply, delivery, and installation of new Ventra fans.</li>
      <li>Allowance has been made for outside air, exhaust ducting and grills.</li>
      <li>Allowance has been made seismic restraints.</li>
      <li>Allowance has been made for commissioning and air balancing.</li>
      <li>Provide workshop drawings, as builts, form 12 and Manuals.</li>
      <li>Provide 12 months defects liability period and servicing.</li>
    </ol>
  </div>
</section>

<section class="page pg5">
  <div class="brand"><span class="brand-dot"></span><span class="brand-name">Tanvale</span></div>
  <div class="band band-ducts" role="img" aria-label="Ceiling cavity with ducts and cabling"></div>
  <h2 class="band-title">SCOPE OF WORKS /</h2>
  <div class="copy exclusions">
    <div class="list-head">Exclusions:</div>
    <ol class="scope-list">
      <li>No allowance has been made to carry out any of the required building works to facilitate the installation of the air conditioning or ventilation equipment.</li>
      <li>Suitable ceiling access panels are to be provided by others for the ongoing maintenance of the air conditioning units and mechanical equipment.</li>
      <li>No allowance has been made for concrete plinths or plant decks.</li>
      <li>No allowance has been made for core holes or concrete cutting.</li>
      <li>No allowance has been made for mains supplies to isolators.</li>
      <li>No allowance has been made for scaffolding or edge protection.</li>
      <li>No allowance has been made for temporary fencing, skip bins or site offices.</li>
      <li>No allowance has been made for cages or screens.</li>
    </ol>
  </div>
</section>

<section class="page pg6">
  <div class="brand"><span class="brand-dot"></span><span class="brand-name">Tanvale</span></div>
  <div class="band band-units" role="img" aria-label="Row of outdoor condensing units against a wall"></div>
  <h2 class="band-title">ACCEPTANCE FORM /</h2>
  <div class="form-row" style="top:124px"><span class="label">QUOTE TOTAL:</span><span class="line"></span></div>
  <div class="form-row" style="top:137px"><span class="label">COMPANY NAME:</span><span class="line"></span></div>
  <div class="form-row" style="top:149px"><span class="label">ABN:</span><span class="line"></span></div>
  <div class="form-row" style="top:162px"><span class="label">ADDRESS:</span><span class="line"></span></div>
  <div class="form-row" style="top:188px"><span class="label">PHONE NUMBER:</span><span class="line"></span></div>
  <div class="form-row" style="top:201px"><span class="label">ACCOUNTS EMAIL:</span><span class="line"></span></div>
  <div class="form-note">I/We accept the terms and conditions as outlined in this quote proposal:</div>
  <div class="form-row" style="top:223px"><span class="label">SIGNATURE:</span><span class="line"></span></div>
  <div class="form-row" style="top:237px"><span class="label">DATE:</span><span class="line"></span></div>
  <div class="form-row" style="top:250px"><span class="label">PRINT NAME:</span><span class="line"></span></div>
</section>

<section class="page pg7">
  <div class="brand"><span class="brand-dot"></span><span class="brand-name">Tanvale</span></div>
  <div class="band band-sunset" role="img" aria-label="Sun over a coastal bay with islands"></div>
  <h2 class="band-title">QUALIFICATION /</h2>
  <div class="copy qual">
    <p>Progress payments shall be made monthly for the value of work completed and accrued. Payment of progress invoices to be paid strictly within thirty (30) days of invoice date.</p>
    <p>We warrant the cost of the equipment supplied by us to the full extent of the Supplier's / Manufacturer's warranty terms and conditions only.</p>
    <p>The warranty does not apply in respect of neglect, damage by fire, flood, abrasion, erosion, corrosion or deterioration due to changes in temperature, exposure to chemicals, energy, radioactivity or other parts or components in the client's systems failing.</p>
    <p>Equipment warranty would commence on the date of commissioning or as specified by the manufacturer.</p>
    <p>We shall undertake the works and rectify any defects in same to your reasonable satisfaction.</p>
    <p>In the event of non-payment of monies owing to us we shall retain ownership of all goods and materials supplied by us for the works and we shall have an unconditional and unfettered right to enter upon premises where equipment and materials are located, retake possession of, resell any equipment and materials redeemed and retain the proceeds of such sale.</p>
  </div>
</section>

<section class="page pg8">
  <div class="brand"><span class="brand-dot"></span><span class="brand-name">Tanvale</span></div>
  <div class="band band-sunset" role="img" aria-label="Coastal view at sunset"></div>
  <h2 class="band-title">BUSINESS TERMS /</h2>
  <div class="terms-col bt-a">
    <h4>1 Definitions, interpretation and precedence</h4>
    <p>1.1 Terms defined in the Agreement Details on page 1 have the meanings given there. Agreement means this supply agreement, its attached annexures and the Quotation. BCIP Act means the Building Industry Fairness (Security of Payment) Act 2017 (Qld) or equivalent legislation. Business Day means a day that is not a Saturday, Sunday or public holiday in the place where the act is done. Intellectual Property Rights include all copyright, designs, trade marks, know-how and confidential information. Quotation means the proposal issued by the Supplier to the Buyer containing an offer of goods or services.</p>
    <h4>1.2 Interpretation</h4>
    <p>References to we, us and our mean the Supplier. References to you and your mean the Buyer named in the Agreement Details.</p>
    <h4>1.3 Order of precedence</h4>
    <p>If there is any inconsistency, the following order applies: (a) special conditions; (b) these terms of supply; (c) the Quotation.</p>
    <h4>2 Quotations and orders</h4>
    <p>2.1 A Quotation is an offer from us to enter into a contract for goods and services. You may accept it expressly in writing or by your conduct. 2.2 A Quotation is valid for 60 days and we may amend it at any time before acceptance. 2.3 Drawings, specifications and catalogue descriptions are approximate only and do not form part of this Agreement.</p>
  </div>
  <div class="terms-col bt-b">
    <h4>3 Your terms</h4>
    <p>3.1 If you submit your own terms with an order, they are not agreed and will not apply unless we notify you directly in writing that we accept them.</p>
    <h4>4 Contract Price</h4>
    <p>4.1 The Supplier will provide the goods and services in return for payment of the Contract Price specified in the Agreement Details. 4.2 All amounts are in Australian dollars unless otherwise stated.</p>
    <h4>5 Invoicing and payment</h4>
    <p>5.1 Payment must be made by the Buyer in accordance with this Agreement and any written instructions given by the Supplier. 5.2 The Supplier will submit invoices to the Buyer following the end of each month for goods delivered and services performed. 5.3 All amounts are payable in full without deduction, set-off or counterclaim. 5.4 No payment is made until the Supplier receives cleared funds. 5.5 The Buyer may dispute an invoice under clause 5.2 by giving written notice within five Business Days, and must still pay any undisputed amount. 5.6 If the Supplier makes a claim under the BCIP Act, the Buyer must respond with a payment schedule within the time the Act allows.</p>
  </div>
</section>

<section class="page pg9">
  <div class="tc tc-a">
    <h4>6 Failure to pay</h4>
    <p>6.1 If the Buyer fails to pay any sums payable by the date on which they become due, then without prejudice to any other remedy the Supplier may: (a) charge interest on all unpaid sums at the rate of 2% per annum above the cash rate; (b) withhold further performance of any obligations until all unpaid sums are paid in full; (c) sell any goods and apply the proceeds to reduce the amount owed; and (d) recover all costs of recovery, including legal costs on an indemnity basis. 6.2 The Supplier's rights under clause 6.1 are subject to any suspension of the Buyer's obligation to pay pending dispute resolution.</p>
    <h4>7 Delivery</h4>
    <p>7.1 Delivery of the goods will take place at the Place of Delivery. 7.2 Any delivery times made known to the Buyer are estimates only. 7.3 The Supplier is not liable for any loss or damage caused to the Buyer by late delivery of the goods or late provision of the services. 7.4 The Buyer will take delivery within 7 days of the Supplier giving notice that the goods are ready. 7.5 If delivery is delayed due to force majeure or any cause beyond our control, we will not be liable for that delay. 7.6 All conditions, guarantees and warranties as to the time of delivery are excluded to the extent permitted by law.</p>
    <h4>8 Buyer's obligations</h4>
    <p>8.1 The Buyer must: (a) ensure the Supplier and its staff have reasonable access to the site; (b) comply with all laws applicable to the site, including workplace health and safety laws; (c) provide accurate information about the site and any hazards; and (d) obtain any approvals required from the owner or building manager.</p>
    <h4>9 Risk</h4>
    <p>9.1 Risk in the goods passes to the Buyer immediately on delivery to the Place of Delivery. 9.2 If the Buyer does not accept delivery when the goods are ready, the goods are deemed delivered and the Supplier may store them at the Buyer's cost.</p>
  </div>
  <div class="tc tc-b">
    <p>Buyer will be liable for all related costs and expenses including storage and insurance. 9.3 The Supplier is not required to deliver the goods until the Buyer has paid for them in full.</p>
    <h4>10 Title</h4>
    <p>10.1 Goods supplied by the Supplier remain the property of the Supplier until the Buyer has paid: (a) the Contract Price for those goods; and (b) all other sums owing to the Supplier on any account. 10.2 Until title passes, the Buyer will: (a) hold the goods as bailee for the Supplier; (b) keep the goods separate and readily identifiable; (c) keep the goods properly stored, protected and insured; and (d) not remove or alter any identifying marks. 10.3 The Supplier may enter any premises where the goods are kept to recover them if payment is overdue.</p>
    <h4>11 PPSA</h4>
    <p>11.1 The Buyer agrees that, unless full payment is received, this Agreement creates a security interest in the goods for the purposes of the Personal Property Securities Act 2009 (Cth). 11.2 The Buyer must do anything reasonably required to register that interest. 11.3 The parties contract out of the provisions of the Act that permit it, including sections 95, 118, 121(4), 130 and 132.</p>
    <h4>12 Confidentiality</h4>
    <p>12.1 The Buyer will keep in strict confidence all technical and commercial know-how, specifications, pricing and processes disclosed by the Supplier, and use them only for this Agreement. 12.2 This obligation survives the end of this Agreement.</p>
    <h4>13 Intellectual Property Rights</h4>
    <p>13.1 All drawings, designs and documents prepared by the Supplier remain its intellectual property. 13.2 The Buyer receives a licence to use them only for the operation and maintenance of the installed systems, once all amounts owing have been paid.</p>
  </div>
</section>

<section class="page pg10">
  <div class="tc tc-a">
    <p>(a) the Buyer has paid all amounts owing; (b) the Buyer will grant the Supplier an irrevocable licence to use any drawings supplied by the Buyer for the works; and (c) the Buyer will obtain all moral rights consents required.</p>
    <h4>14 Supplier warranties</h4>
    <p>14.1 The Supplier makes the warranties set out in the Annexure in respect of the goods and services supplied.</p>
    <h4>15 Liability and indemnity</h4>
    <p>15.1 To the maximum extent permitted by law: (a) no statement or recommendation made by the Supplier will be a representation or warranty unless made in writing; (b) all conditions and warranties that can be excluded are excluded; and (c) the Supplier is not liable for any indirect or consequential loss, loss of profit or loss of revenue. 15.2 Where the Australian Consumer Law applies and liability cannot be excluded, the Supplier's liability is limited to replacing or repairing the goods or supplying the services again. 15.3 The Buyer indemnifies the Supplier against any claim arising from the Buyer's breach of this Agreement.</p>
    <h4>16 Disputes</h4>
    <p>16.1 The parties agree to work together to quickly settle any dispute. If it cannot be resolved within 14 days of written notice, senior representatives will meet in good faith. 16.2 Disputes not settled in that time may be referred to mediation before any court proceedings begin.</p>
    <h4>17 Termination</h4>
    <p>17.1 The Supplier may suspend performance of, or end, this Agreement without liability if: (a) the Buyer breaches this Agreement and fails to remedy that breach within 7 days of notice; or (b) the Buyer's business fails. 17.2 The Buyer's business fails if it becomes insolvent, enters administration, makes an arrangement with its creditors or ceases to trade.</p>
  </div>
  <div class="tc tc-b">
    <p>(d) any third party takes possession of any of the Buyer's property; or (e) the Buyer stops carrying on business. 17.3 On termination all amounts owing become immediately payable.</p>
    <h4>18 GST</h4>
    <p>18.1 If any supply made under this Agreement is a taxable supply, the consideration for that supply is increased by the amount of GST payable. 18.2 Words used in this clause have the meaning given in the A New Tax System (Goods and Services Tax) Act 1999 (Cth).</p>
    <h4>19 Waiver</h4>
    <p>19.1 A party waives a right only if it does so in writing. A failure or delay in exercising a right is not a waiver of that right or of any later breach.</p>
    <h4>20 Entire agreement</h4>
    <p>20.1 This Agreement is the entire agreement between the Supplier and the Buyer and supersedes all earlier proposals, negotiations and understandings.</p>
    <h4>21 Variations</h4>
    <p>21.1 Alterations or variations to this Agreement or any specifications will not be legally binding unless agreed in writing by both parties.</p>
    <h4>22 Notices</h4>
    <p>22.1 All notices must be in writing and sent to the address in the Agreement Details. 22.2 A notice is received: (a) if delivered by hand, on delivery; (b) if sent by post, 3 Business Days after posting; (c) if sent by email, when it enters the recipient's system. 22.3 A notice received after 5.00pm is taken to be received on the next Business Day.</p>
    <h4>23 Governing law</h4>
    <p>23.1 This Agreement will be governed by the laws of the State of Queensland, and the parties submit to the exclusive jurisdiction of its courts.</p>
    <h4>24 Subcontracting and assignment</h4>
    <p>24.1 The Supplier may assign or subcontract all or any part of its obligations under this Agreement without the prior written agreement of the Buyer.</p>
  </div>
</section>

<section class="page pg11">
  <div class="back-photo" role="img" aria-label="Technician with his dog leaning on an outdoor condensing unit"></div>
  <div class="back-brand"><span class="brand-dot"></span><span class="brand-name">Tanvale</span></div>
  <div class="contact contact-a">
    PH: 0400 615 238 &nbsp;&nbsp; E: admin@tanvale.com.au<br>
    A: 12 Coral Way, Harbourview, QLD 4802<br>
    A: 4/9 Mill Street, Eastfield QLD 4551
  </div>
  <div class="contact contact-b">
    RHL licence: AU50172<br>
    QBCC licence: 15099821<br>
    QLD Electrical licence: 80341
  </div>
  <div class="badge" role="img" aria-label="Certification badge"></div>
</section>

</body>
</html>
```